Modern/Bold/Unique Prenatal Vitamin label redesign

We are in need of a design update for our Prenatal Vitamin label. We want to modernize our label and give it a fresh feel.
It should bring a feeling of fun, joy, and sophistication, but also be bold/edgy/unique and portray Trust and Authority. Our buyers are mainly mothers in the age range of 25-34 who are pregnant or breastfeeding.
I will attach our current label design, as well as some inspiration to go off of.
We like the idea of having a clean, easy to read label label with bold/vibrant colors and fonts. We like the idea of having some retro vibes in it as well
Please see the attached artwork for design inspiration (New Design Idea). We like the idea of having a pregnant mother image like the attachment on the label, with the rest of the label being white. Please come up with a unique drawing/image for the design. We cannot use a copied image or stock image.
We look forward to working with you!

```html
<!DOCTYPE html>
<html lang="en">
<head>
<meta charset="utf-8">
<title>Bloom Nest Prenatal Plus Label</title>
<link href="https://fonts.googleapis.com/css2?family=Montserrat:wght@300;400;700;800;900&display=swap" rel="stylesheet">
<style>
  :root {
    --red-orange: #ef4923;
    --orange: #f47b20;
    --amber: #f9a11b;
    --sun: #fbbd13;
    --cream: #fde6b4;
    --peach: #f7a46f;
    --white: #ffffff;
    --ink: #000000;
    --gold-dark: #c07f12;
    --gold-light: #e3a814;
    --figure-a: #d4553f;
    --figure-b: #f0744a;
  }
  * { margin: 0; padding: 0; box-sizing: border-box; }
  html, body { width: 686px; height: 1200px; overflow: hidden; }
  body { font-family: 'Montserrat', sans-serif; }
  .label {
    position: relative;
    width: 686px;
    height: 1200px;
    overflow: hidden;
    background:
      radial-gradient(ellipse 330px 260px at 300px 690px, var(--cream) 0%, rgba(253,230,180,0) 100%),
      linear-gradient(170deg, var(--red-orange) 0%, var(--orange) 28%, var(--amber) 45%, var(--sun) 62%, var(--amber) 85%, var(--orange) 100%);
  }
  .waves { position: absolute; left: 0; top: 600px; width: 686px; height: 520px; }
  .brand {
    position: absolute;
    top: 112px;
    width: 100%;
    text-align: center;
    color: var(--white);
    font-weight: 900;
    font-size: 62px;
    letter-spacing: 0.5px;
  }
  .rule {
    position: absolute;
    left: 72px; top: 322px;
    width: 542px; height: 4px;
    background: var(--white);
  }
  .product-name {
    position: absolute;
    left: 68px; top: 340px;
    width: 550px;
    text-align: center;
    color: var(--white);
    font-weight: 800;
    font-size: 94px;
    line-height: 1;
    letter-spacing: -1px;
    text-shadow: 4px 6px 10px rgba(150, 70, 10, 0.45);
  }
  .plus-pill {
    position: absolute;
    left: 360px; top: 444px;
    width: 254px; height: 86px;
    border-radius: 24px;
    background: var(--white);
    box-shadow: 4px 6px 12px rgba(150, 70, 10, 0.35);
    display: flex; align-items: center; justify-content: center;
  }
  .plus-pill span {
    font-weight: 800;
    font-size: 78px;
    line-height: 1;
    background: linear-gradient(90deg, var(--gold-dark), var(--gold-light), var(--gold-dark));
    -webkit-background-clip: text;
    background-clip: text;
    color: transparent;
    letter-spacing: -1px;
  }
  .mother-art {
    position: absolute;
    left: 64px; top: 482px;
    width: 316px; height: 626px;
  }
  .count-card {
    position: absolute;
    left: 481px; top: 861px;
    width: 205px; height: 212px;
    background: var(--white);
    border-radius: 56px 0 0 56px;
    text-align: center;
    padding-left: 22px;
  }
  .count-number {
    margin-top: 16px;
    font-weight: 800;
    font-size: 86px;
    line-height: 1;
    color: var(--red-orange);
  }
  .count-unit {
    font-weight: 300;
    font-size: 33px;
    line-height: 0.98;
    color: var(--ink);
    margin-top: 4px;
  }
  .supplement-tag {
    display: inline-block;
    margin-top: 8px;
    background: var(--ink);
    color: var(--white);
    font-size: 10px;
    font-weight: 400;
    padding: 1px 4px;
  }
  .tagline-band {
    position: absolute;
    left: 0; top: 1108px;
    width: 686px; height: 50px;
    background: var(--white);
    display: flex; align-items: center; justify-content: center;
    color: var(--red-orange);
    font-size: 22.5px;
    font-weight: 400;
    white-space: nowrap;
  }
  .base-band {
    position: absolute;
    left: 0; top: 1158px;
    width: 686px; height: 42px;
    background: linear-gradient(90deg, var(--red-orange), var(--orange));
  }
</style>
</head>
<body>
<div class="label">
  <svg class="waves" viewBox="0 0 686 520" aria-hidden="true">
    <path d="M0 84 C80 140 180 170 260 150 C330 130 360 60 470 30 C560 6 630 20 686 22 L686 45 C600 40 520 50 430 90 C340 130 300 240 200 270 C120 290 40 260 0 240 Z" fill="var(--orange)" opacity="0.75"/>
    <path d="M0 108 C80 160 180 190 260 170 C330 150 380 90 470 58 C560 32 630 44 686 46 L686 190 C600 165 520 150 430 170 C340 190 300 260 200 290 C120 310 40 290 0 255 Z" fill="var(--peach)" opacity="0.85"/>
    <path d="M0 255 C40 290 120 310 200 290 C300 260 350 200 450 180 C540 160 620 175 686 190 L686 212 C620 198 540 186 450 204 C350 225 300 290 200 310 C120 322 40 300 0 278 Z" fill="var(--cream)" opacity="0.9"/>
  </svg>

  <div class="brand">Bloom Nest</div>

  <div class="rule"></div>
  <h1 class="product-name">PRENATAL</h1>
  <div class="plus-pill"><span>PLUS</span></div>

  <svg class="mother-art" viewBox="0 0 316 626" role="img" aria-label="Colourful illustration of a pregnant mother silhouette with white outline">
    <defs>
      <linearGradient id="figureFill" x1="0" y1="0" x2="0" y2="1">
        <stop offset="0" stop-color="var(--figure-a)"/>
        <stop offset="1" stop-color="var(--figure-b)"/>
      </linearGradient>
    </defs>
    <rect x="0" y="0" width="316" height="626" rx="60" fill="url(#figureFill)"/>
  </svg>

  <div class="count-card">
    <div class="count-number">90</div>
    <div class="count-unit">Veggie<br>Capsules</div>
    <div class="supplement-tag">DIETARY SUPPLEMENT</div>
  </div>

  <div class="tagline-band">ONCE DAILY PREMIUM MULTIVITAMIN FOR MAMA &amp; BABY</div>
  <div class="base-band"></div>
</div>
</body>
</html>
```